Stationary Design

Harbor Stagecraft Works, Inc
27450 Lindell Ave Ste 3, Santa Fe Springs, CA 90418
Office: 213-555-0187 Email: admin@hswinc.example

Industry/Entity Type

Entertainment

Colors
0054AA
0677BA
7BADD7
CADEEF
E8F1F8

```html
<!DOCTYPE html>
<html lang="en">
<head>
<meta charset="utf-8">
<title>Harbor Stagecraft Works – Letterhead</title>
<link rel="stylesheet" href="https://fonts.googleapis.com/css2?family=Arimo:wght@400;700&family=Questrial&display=swap">
<style>
  :root {
    --brand-blue: #0054AA;
    --accent-grey: #939598;
    --paper: #f4f4f4;
    --backdrop: #e2e2e2;
    --text: #4d4d4d;
    --heading: #444444;
    --signature-tone: #c9c9c9;
  }
  * { box-sizing: border-box; margin: 0; padding: 0; }
  html, body { width: 1110px; height: 1200px; overflow: hidden; }
  body { background: var(--backdrop); position: relative; font-family: "Arimo", Arial, sans-serif; }

  .letterhead {
    position: absolute; left: 141px; top: 20px;
    width: 828px; height: 1160px;
    background: var(--paper);
    box-shadow: 0 6px 24px rgba(0,0,0,.18);
    overflow: hidden;
  }
  .swoosh { position: absolute; left: 0; top: 0; width: 828px; height: 1160px; }

  .brand {
    position: absolute; top: 86px; left: 0; width: 100%;
    display: flex; justify-content: center; align-items: center; gap: 10px;
  }
  .brand-dot { width: 26px; height: 26px; border-radius: 50%; background: var(--accent-grey); }
  .brand-name { font-family: "Arimo", Arial, sans-serif; font-weight: 700; font-size: 21px; color: var(--brand-blue); letter-spacing: .3px; }

  .greeting {
    position: absolute; left: 75px; top: 356px;
    font-family: "Questrial", "Century Gothic", sans-serif; font-weight: 400;
    font-size: 19px; color: var(--heading); -webkit-text-stroke: .4px var(--heading);
  }
  .letter-body { position: absolute; left: 73px; top: 408px; width: 680px; }
  .letter-body p { font-size: 13.9px; line-height: 16.8px; color: var(--text); margin-bottom: 15.7px; }

  .closing {
    position: absolute; left: 75px; top: 758px;
    font-family: "Questrial", "Century Gothic", sans-serif;
    font-size: 10.5px; color: var(--heading); -webkit-text-stroke: .3px var(--heading);
  }
  .signature { position: absolute; left: 74px; top: 806px; width: 136px; height: 40px; background: var(--signature-tone); border-radius: 3px; }

  .contact {
    position: absolute; right: 75px; top: 1027px;
    padding-right: 14px; border-right: 1px solid var(--accent-grey);
    text-align: right; color: var(--text); font-size: 13px; line-height: 16.8px;
  }
  .contact-line { display: flex; justify-content: flex-end; align-items: center; gap: 5px; }
  .contact-line svg { width: 11px; height: 11px; flex: none; }
  .address { margin-top: 10px; padding-right: 0; }
</style>
</head>
<body>
  <main class="letterhead">
    <svg class="swoosh" viewBox="0 0 828 1160" aria-hidden="true">
      <path d="M480,0 Q740,35 828,180 L828,166 Q728,30 508,0 Z" fill="var(--accent-grey)"/>
      <path d="M525,0 L828,0 L828,155 Q722,28 525,0 Z" fill="var(--brand-blue)"/>
      <path d="M0,979 Q130,1115 348,1160 L318,1160 Q120,1108 0,994 Z" fill="var(--accent-grey)"/>
      <path d="M0,1005 Q112,1120 303,1160 L0,1160 Z" fill="var(--brand-blue)"/>
    </svg>

    <header class="brand">
      <span class="brand-dot"></span>
      <span class="brand-name">Harbor Stagecraft Works</span>
    </header>

    <h1 class="greeting">Dear Mr. Harlow,</h1>

    <section class="letter-body">
      <p>Lorem ipsum dolor sit amet, consectetuer adipiscing elit, sed diam nonmmy nibh euismod tincidunt ut laor eet dolore magna aliquam erat volutpat. Ut wisi enim ad minim veniam, quis nostrud exerci tationmcorper suscipit lobortis nisl ut aliquip ex ea commodo consequat. Duis autem vel eum iriure dolor in hendrerit in vulputate velit esse molestie consequat, vel illum dolore eu feugiat</p>
      <p>Rorem ipsum dolor sit amet, consectetuer adipiscing elit, sed diam nonmmy nibh euismod tincidunt ut laor eet dolore magna aliquam erat volutpat. Ut wisi enim ad minim veniam, quis nostrud exerci tationmcorper suscipit lobortis nisl ut aliquip ex ea commodo consequat. Duis autem vel eum iriure dolor in hendrerit in vulputate velit esse molest</p>
      <p>Dorem ipsum dolor sit amet, consectetuer adipiscing elit, sed diam nonmmy nibh euismod tincidunt ut laor eet dolore magna aliquam erat volutpat. Ut wisi enim ad minim veniam, quis nostrud exerci tationmcorper suscipit lobortis nisl ut aliquip ex ea commodo consequat. Duis autem vel eum iriure dolor in hendrerit in suscipit lobortis nisl ut aliquip ex ea commodo consequat. Duis autem vel eum iriure dolor in hendrerit in vulputate velit esse molestie consequat, vel illum</p>
      <p>Sorem ipsum dolor sit amet, consectetuer adipiscing elit, sed diam nonmmy nibh euismod tincidunt ut laor eet dolore magna aliquam erat volutpat. Ut wisi enim ad minim veniam, quis nostrud exerci tationmcorper suscipit lobortis nisl ut aliquip ex ea commodo consequat. Duis autem vel eum iriure dolor in</p>
    </section>

    <p class="closing">Sincerely,</p>
    <div class="signature" role="img" aria-label="Handwritten signature of the sender"></div>

    <footer class="contact">
      <div class="contact-line">213-555-0187
        <svg viewBox="0 0 12 12"><path d="M3,1 L5,3.5 L4,5 Q5,7 7,8 L8.5,7 L11,9 L9.5,11 Q4,10.5 1,2.5 Z" fill="var(--brand-blue)"/></svg>
      </div>
      <div class="contact-line">admin@hswinc.example
        <svg viewBox="0 0 12 12"><rect x="1" y="3" width="10" height="7" fill="var(--brand-blue)"/><path d="M1,3 L6,7 L11,3" stroke="#fff" stroke-width="1" fill="none"/></svg>
      </div>
      <div class="contact-line">www.hswinc.example
        <svg viewBox="0 0 12 12"><circle cx="6" cy="6" r="5" fill="var(--brand-blue)"/><ellipse cx="6" cy="6" rx="2.2" ry="5" stroke="#fff" stroke-width=".8" fill="none"/><path d="M1,6 H11" stroke="#fff" stroke-width=".8"/></svg>
      </div>
      <address class="address" style="font-style:normal">27450 Lindell Ave Ste 3<br>Santa Fe Springs, CA 90418</address>
    </footer>
  </main>
</body>
</html>
```